Brochure design for HVAC Company

A classic tri-fold brochure design for an air conditioning, refrigeration, and heating company. Would like the designs to be simple (uncluttered), professional, and pull in the logo colors. Attached is the logo and a business card designs. The company name is Bluefinch Ridge Air Conditioning, Refrigeration, and Heating.

Target Market(s)

Businesses normally food establishments for refrigeration and ice machines. Looking to sell them on maintenance plan: Gold, Silver, and Bronze. The material should help them to understand the services offered: Maintenance, Servicing and Troubleshooting, and Installations of ice machines, commercial refrigeration, and walk-in freezers and air conditioning (duct, ductless, and rooftop)

Industry/Entity Type

Hvac

Font styles to use
Sans Serif

Requirements
Must have
• Include standard information, such as company name, at least two types of contact information (phone, email and post office address), a logo and tagline. It should also include a headline on the front and two or three brief items outlining benefits your organization can provide.
• Tagline is approximately 14 words and 66 characters.
• Looking to inform customers of services offered: maintenance three plans gold, silver, and bronze, servicing and troubleshooting, and installation.
• Products Serviced, maintained, and installed: Commercial refrigeration, Ice Machines, Air Conditioning (both duct, ductless, and rooftop), walk in freezers.
• Call to action is $100 off on signed maintenance contract. $50 off on first service call.
• Use lorem ipsum text to complement the details of the above information. I will add it later before printing.
• Use logo color scheme and any other colors that complement it.
• Would like this to be a word template.
Nice to have
• Can you make this a Microsoft Word template? Sketch is good, or adobe cs4 format.
Should not have
• Photos should NOT be focused on the homeowner. Should BE focused on the commercial side of the business. Photos can be from any of these product areas: commercial refrigeration, ice machine, walk in freezer boxes, and light roof top ac and heating units.

```html
<!DOCTYPE html>
<html lang="en">
<head>
<meta charset="utf-8">
<title>Bluefinch Ridge – Brochure Cover Panel</title>
<link rel="stylesheet" href="https://fonts.googleapis.com/css2?family=Montserrat:wght@400;700;800&display=swap">
<style>
  :root {
    --brand-blue: #3456a6;
    --brand-blue-deep: #2c4a94;
    --brand-orange: #e2612a;
    --paper: #f4f4f2;
    --stage: #e6e8ee;
    --ink-light: #ffffff;
  }
  * { box-sizing: border-box; margin: 0; padding: 0; }
  html, body {
    width: 1200px;
    height: 900px;
    overflow: hidden;
    background: var(--stage);
    font-family: "Montserrat", sans-serif;
  }
  .canvas {
    width: 1200px;
    height: 900px;
    display: flex;
    align-items: center;
    justify-content: center;
  }
  .cover-panel {
    width: 372px;
    height: 840px;
    display: flex;
    flex-direction: column;
    background: var(--paper);
    box-shadow: 0 10px 30px rgba(30, 40, 70, 0.18);
  }
  .cover-photo {
    height: 452px;
    background: linear-gradient(180deg, #b89a78 0%, #d9d6cf 12%, #c8ccc9 40%, #b9a98e 60%, #d8dad6 82%, #a9adab 100%);
  }
  .brand-band {
    height: 112px;
    background: var(--brand-blue);
    display: flex;
    flex-direction: column;
    align-items: center;
    justify-content: center;
    gap: 8px;
    color: var(--ink-light);
  }
  .brand-lockup {
    display: flex;
    align-items: center;
    gap: 10px;
  }
  .brand-dot {
    width: 18px;
    height: 18px;
    border-radius: 50%;
    background: var(--brand-orange);
  }
  .brand-name {
    font-weight: 800;
    font-size: 25px;
    letter-spacing: 0.5px;
    text-transform: uppercase;
  }
  .brand-services {
    font-weight: 700;
    font-size: 8.5px;
    letter-spacing: 1.4px;
    text-transform: uppercase;
  }
  .headline-area {
    flex: 1;
    padding: 34px 40px 0;
    color: var(--brand-blue);
  }
  .headline {
    font-size: 27px;
    line-height: 1.12;
    font-weight: 400;
  }
  .headline-emphasis {
    display: block;
    color: var(--brand-orange);
    font-weight: 800;
    text-transform: uppercase;
    font-size: 24px;
  }
  .web-bar {
    height: 62px;
    background: var(--brand-orange);
    color: var(--ink-light);
    display: flex;
    align-items: center;
    justify-content: center;
    font-size: 21px;
    font-weight: 400;
    letter-spacing: 0.3px;
  }
</style>
</head>
<body>
  <main class="canvas">
    <article class="cover-panel">
      <div class="cover-photo" role="img" aria-label="Photo of a supermarket open refrigerated display case stocked with packaged food"></div>
      <header class="brand-band">
        <div class="brand-lockup">
          <span class="brand-dot"></span>
          <span class="brand-name">Bluefinch Ridge</span>
        </div>
        <p class="brand-services">Air Conditioning · Refrigeration · Heating</p>
      </header>
      <section class="headline-area">
        <h1 class="headline">
          Contrary to
          <span class="headline-emphasis">Popular belief, Lorem Ipsum is</span>
          not simply random text
        </h1>
      </section>
      <footer class="web-bar">bluefinchridgehvac.com</footer>
    </article>
  </main>
</body>
</html>
```